Maple Hollow Canine Massage Needs a Business Card Design

Maple Hollow Canine Massage is a new therapeutic canine massage company located in Nederland, Colorado. I need a business card design that include my logo and basic contact information.

Target Market(s)

Pet owners, veterinarians

Industry/Entity Type

Business

Contact Information for Business Card

Lydia Ferrow, CCMT
303.518.7269
lydia@maplehollowmassage.example
www.maplehollowmassage.example

Colors
6c459b
886aae
b8a6cd
a64599
b768aa
d3a5cc
fbed22

Requirements
Must have
• Font should be similar to font in logo.

```html
<!DOCTYPE html>
<html lang="en">
<head>
<meta charset="utf-8">
<title>Maple Hollow Canine Massage – Business Card</title>
<link rel="stylesheet" href="https://fonts.googleapis.com/css2?family=Source+Sans+3:wght@400;600&display=swap">
<style>
  :root {
    --stage: #4d4d4d;
    --card-white: #ffffff;
    --plum: #4b2a5e;
    --lavender: #b08bc7;
    --gold: #f2c14e;
    --ink: #4a4a4a;
    --rule: #cfcfcf;
    --art-tone: rgba(255,255,255,0.16);
  }
  * { box-sizing: border-box; margin: 0; padding: 0; }
  html, body { width: 1105px; height: 1200px; overflow: hidden; }
  body {
    background: var(--stage);
    font-family: "Source Sans 3", "Myriad Pro", Arial, sans-serif;
    position: relative;
  }
  .card {
    position: absolute;
    left: 162px;
    width: 780px;
    height: 446px;
    overflow: hidden;
  }
  .card-front { top: 129px; background: var(--card-white); }
  .card-back  { top: 625px; background: var(--plum); }

  /* front */
  .brand {
    position: absolute;
    left: 95px; top: 88px;
    width: 220px;
    text-align: center;
  }
  .brand-dot {
    width: 150px; height: 150px;
    margin: 0 auto;
    border-radius: 50%;
    background: var(--lavender);
  }
  .brand-name {
    margin-top: 16px;
    color: var(--plum);
    font-weight: 600;
    font-size: 19px;
    line-height: 1.2;
  }
  .divider {
    position: absolute;
    left: 346px; top: 130px;
    width: 1px; height: 150px;
    background: var(--rule);
  }
  .contact { position: absolute; left: 377px; top: 132px; }
  .person {
    color: var(--plum);
    font-weight: 600;
    font-size: 29px;
    line-height: 1;
    margin-bottom: 26px;
  }
  .person .credential { font-weight: 400; font-size: 22px; }
  .contact-line {
    display: flex; align-items: center; gap: 10px;
    color: var(--ink);
    font-size: 20px;
    line-height: 30px;
  }
  .contact-line svg { width: 17px; height: 17px; fill: var(--plum); flex: none; }
  .accent-rule {
    position: absolute; left: 0; right: 0; top: 409px;
    height: 4px; background: var(--gold);
  }
  .base-band {
    position: absolute; left: 0; right: 0; top: 416px; bottom: 0;
    background: var(--plum);
  }

  /* back */
  .dog-art {
    position: absolute;
    left: 218px; top: 112px;
    width: 340px; height: 222px;
    background: var(--art-tone);
    border-radius: 6px;
  }
  .back-url {
    position: absolute; left: 0; right: 0; top: 375px;
    text-align: center;
    color: #ffffff;
    font-size: 21px;
    letter-spacing: 3px;
  }
</style>
</head>
<body>
  <section class="card card-front">
    <div class="brand">
      <div class="brand-dot"></div>
      <div class="brand-name">Maple Hollow Canine Massage</div>
    </div>
    <div class="divider"></div>
    <div class="contact">
      <p class="person">Lydia Ferrow, <span class="credential">CCMT</span></p>
      <p class="contact-line">
        <svg viewBox="0 0 24 24"><path d="M6.6 10.8a15.2 15.2 0 0 0 6.6 6.6l2.2-2.2a1 1 0 0 1 1-.25 11.4 11.4 0 0 0 3.6.57 1 1 0 0 1 1 1V20a1 1 0 0 1-1 1A17 17 0 0 1 3 4a1 1 0 0 1 1-1h3.5a1 1 0 0 1 1 1c0 1.25.2 2.45.57 3.57a1 1 0 0 1-.25 1z"/></svg>
        303.518.7269
      </p>
      <p class="contact-line">
        <svg viewBox="0 0 24 24"><path d="M2 5h20v14H2z M2 5l10 8 10-8" fill="none" stroke="#4b2a5e" stroke-width="2"/><path d="M2 5h20l-10 8z"/></svg>
        lydia@maplehollowmassage.example
      </p>
      <p class="contact-line">
        <svg viewBox="0 0 24 24"><circle cx="12" cy="12" r="10" fill="none" stroke="#4b2a5e" stroke-width="2"/><path d="M2 12h20M12 2c3 3 3 17 0 20M12 2c-3 3-3 17 0 20" fill="none" stroke="#4b2a5e" stroke-width="1.6"/></svg>
        www.maplehollowmassage.example
      </p>
    </div>
    <div class="accent-rule"></div>
    <div class="base-band"></div>
  </section>

  <section class="card card-back">
    <div class="dog-art" role="img" aria-label="White illustration of a walking dog drawn as a star constellation"></div>
    <p class="back-url">www.maplehollowmassage.example</p>
  </section>
</body>
</html>
```